Rack card for a integrative medical practice

Need an eye-catching rack card with our logo with content as provided. We have a membership based holistic medical practice which incorporates western and holistic medicine. We would like to focus on wellness and healthy lifestyle. See uploaded files for what is included in the membership. Would like 2 page rack card color on both sides. Logo must be on the front.

Target Market(s)

People looking for alternative medicine, healthy lifestyle.

Industry/Entity Type

Health and Wellness

Colors
00AB8E
00BBA5
67D7C9
C6EFE9
E9F9F6

Requirements
Must have
• Must spark interest at first sight. Clear message.
Nice to have
• Warm, bright and positive vibe. Organic, neutral and earthy colors.
Should not have
• Traditional medical practice vibe (cold, formal, industrial). No PINK except the logo.

```html
<!DOCTYPE html>
<html lang="en">
<head>
<meta charset="utf-8">
<title>Sable Grove Health &amp; Wellness – Rack Card</title>
<link rel="stylesheet" href="https://fonts.googleapis.com/css2?family=Cinzel:wght@500;600;700&family=Arimo:wght@400;700&display=swap">
<style>
  :root {
    --page-bg: #e4e5e8;
    --card-cream: #f6ece4;
    --card-cream-deep: #efe0d4;
    --brand-teal: #00ab8e;
    --brand-teal-light: #00bba5;
    --ink-green: #0f2a22;
    --body-text: #3b4a44;
    --tagline-text: #4a4f4c;
    --white: #ffffff;
  }
  * { box-sizing: border-box; margin: 0; padding: 0; }
  html, body { width: 1200px; height: 1149px; overflow: hidden; }
  body { background: var(--page-bg); position: relative; font-family: "Arimo", Arial, sans-serif; }

  .rack-card {
    position: absolute; top: 140px; width: 387px; height: 870px;
    background: radial-gradient(ellipse at 40% 30%, var(--card-cream) 0%, var(--card-cream-deep) 100%);
    overflow: hidden;
  }
  .rack-card--front { left: 137px; }
  .rack-card--back { left: 594px; }

  .card-shapes { position: absolute; inset: 0; }

  .logo-name {
    position: absolute; left: 0; width: 100%; text-align: center;
    font-family: "Cinzel", Georgia, serif; font-weight: 700; font-size: 22px;
    color: var(--ink-green); letter-spacing: 1px;
  }
  .rack-card--front .logo-name { top: 129px; }
  .rack-card--back .logo-name { top: 715px; }

  .front-title {
    position: absolute; top: 272px; left: 0; width: 100%; text-align: center;
    font-family: "Cinzel", Georgia, serif; font-weight: 700; font-size: 42px;
    line-height: 47px; color: var(--ink-green);
  }
  .front-rule {
    position: absolute; top: 470px; left: 60px; width: 267px; height: 1.5px;
    background: var(--ink-green); opacity: .75;
  }
  .front-tagline {
    position: absolute; top: 480px; left: 78px; width: 231px; text-align: center;
    font-size: 16px; line-height: 20px; color: var(--tagline-text);
  }
  .photo-frame {
    position: absolute; top: 593px; left: 69px; width: 248px; height: 165px;
    border: 1.5px solid var(--ink-green); border-radius: 14px; padding: 5px;
  }
  .photo-frame__image {
    width: 100%; height: 100%; border-radius: 10px;
    background: linear-gradient(120deg, #d9b9c2 0%, #f3ece9 45%, #e8d4cc 70%, #c9969f 100%);
  }
  .address-box {
    position: absolute; top: 790px; left: 58px; width: 271px; height: 80px;
    background: var(--brand-teal); border-radius: 20px 20px 0 0;
    color: var(--white); font-weight: 700; font-size: 17px; line-height: 22px;
    text-align: center; padding-top: 11px;
  }

  .membership-heading {
    position: absolute; top: 34px; left: 39px; width: 308px; text-align: center;
    font-family: "Cinzel", Georgia, serif; font-weight: 600; font-size: 27px;
    line-height: 36px; color: var(--white);
  }
  .benefit-list {
    position: absolute; top: 179px; left: 40px; width: 318px; list-style: none;
  }
  .benefit {
    position: relative; padding-left: 11px; margin-bottom: 14px;
    font-size: 16.5px; line-height: 21px; color: var(--body-text);
  }
  .benefit::before { content: "•"; position: absolute; left: 0; }
</style>
</head>
<body>

  <section class="rack-card rack-card--front">
    <svg class="card-shapes" width="387" height="870" viewBox="0 0 387 870" aria-hidden="true">
      <rect x="93" y="0" width="200" height="85" fill="var(--brand-teal)"/>
      <circle cx="193" cy="143" r="109" fill="var(--card-cream)"/>
      <circle cx="193" cy="143" r="101" fill="none" stroke="var(--brand-teal-light)" stroke-width="2"/>
    </svg>
    <div class="logo-name">Sable Grove</div>
    <h1 class="front-title">SABLE GROVE<br>HEALTH<br>&amp;<br>WELLNESS</h1>
    <div class="front-rule"></div>
    <p class="front-tagline">A Direct Primary Care Practice Focused On A More Holistic And Personal Approach To Medicine.</p>
    <div class="photo-frame">
      <div class="photo-frame__image" role="img" aria-label="Photo of a person in white linen seated cross-legged among cushions, hand on heart, in a calm meditation pose"></div>
    </div>
    <div class="address-box">1420 Linden Ave., STE 2B<br>Brookfield</div>
  </section>

  <section class="rack-card rack-card--back">
    <svg class="card-shapes" width="387" height="870" viewBox="0 0 387 870" aria-hidden="true">
      <path d="M39 0 H347 V127 Q347 157 317 157 H69 Q39 157 39 127 Z" fill="var(--brand-teal)"/>
      <rect x="83" y="757" width="220" height="113" fill="var(--brand-teal)"/>
      <circle cx="194" cy="729" r="109" fill="var(--card-cream)"/>
      <circle cx="194" cy="729" r="100" fill="none" stroke="var(--brand-teal-light)" stroke-width="2"/>
    </svg>
    <h2 class="membership-heading">WHAT'S INCLUDED<br>IN YOUR<br>MEMBERSHIP</h2>
    <ul class="benefit-list">
      <li class="benefit">Unlimited office visits with no copay</li>
      <li class="benefit">Direct communication with your doctor</li>
      <li class="benefit">Discounted labs, imaging and medications</li>
      <li class="benefit">Free initial acupuncture session ($250 value).</li>
      <li class="benefit">2 BodyScan testings per year ($100 value)</li>
      <li class="benefit">Discounts for supplements and health products in the clinic</li>
      <li class="benefit">Discounts for iv vitamin infusion therapy</li>
      <li class="benefit">Personalized nutrition plan after advanced testing such as gut microbiome, hormonal, metabolism test, etc.</li>
    </ul>
    <div class="logo-name">Sable Grove</div>
  </section>

</body>
</html>
```